Nine Lanterns Quill House Book Cover for: "Growing Older Wisely"

We are a publishing company who plans to launch the book, Growing Older Wisely, A Handy Compact Manual for Legal, Financial and Emotional Health in late 2018. We desire a book cover that creates interest, looks professional and can draw readers to open and purchase this book. Growing Older Wisely is an invaluable, self-help book which provides Generation X, Baby Boomers and their families with the following information: steps to obtain valid, reliable wills and trusts, identify and pay for health care, address end of life care and manage grief. (Please see the attached book description for more information about the book contents). The cover needs to have a "wellness", health and healing emphasis but it should not be morbid. Instead, the cover should have an uplifting, inviting and engaging feeling.

The designer should use Photoshop to develop the 5 x 7 cover. Please design the front, back cover and spine using the attached suggested layout as a guide. Use colors that complement the background colors in the author's photo and the logo for the front and back colors. Feel free to change the colors of the black rectangles on the front of the book. We are looking for a design to be added using the suggested layouts but we are open to modifications of the layout provided that all the content in the attachments are used. Below are the specifications needed for the cover:

-Use Photoshop
-Develop a front and back cover for a 5 x 7 format book
-Include the book title, subtitle and author name on the front cover as noted on the front cover attachment
-Include a book title and author names on the spine of the cover
-Use full bleed background if appropriate
-Color correct and resize images as necessary
-Insert logo and publisher’s imprint on spine and back cover as noted in attachments

For designers who are successful with this contest, we will primarily consider you for future projects.

Thanks!

Target Market(s)

Generation X, Baby Boomers and their families

Industry/Entity Type

Book Publisher

Font styles to use
Sans Serif

Colors

Designer to choose colors to be used in the design.

Requirements
Must have
• The designer should use Photoshop to develop the 5 x 7 cover. Please design the front, back cover and spine using the attached suggested layout as a guide. Use colors that complement the background colors in the author's photo and the logo for the front and back colors. Feel free to change the colors of the black rectangles on the front of the book. We are looking for a design to be added using the suggested layouts but we are open to modifications of the layout provided that all the content in the attachments are used. Below are the specifications needed for the cover:
• -Use Photoshop
• -Develop a front and back cover for a 5 x 7 format book
• -Include the book title, subtitle and author name on the front cover as noted on the front cover attachment
• -Include a book title and author names on the spine of the cover
• -Use full bleed background if appropriate
• -Color correct and resize images as necessary
• -Insert logo and publisher’s imprint on spine and back cover as noted in attachments
Nice to have
• N/A
Should not have
• The design should not specifically duplicate the layout samples or include pictures of persons on the cover. We have provided those as a guide; we are looking for innovation and professionalism.

```html
<!DOCTYPE html>
<html lang="en">
<head>
<meta charset="utf-8">
<title>Growing Older Wisely – Book Cover</title>
<link rel="stylesheet" href="https://fonts.googleapis.com/css2?family=Oswald:wght@600;700&family=Roboto+Condensed:wght@300;400&family=Tinos:ital,wght@0,400;0,700;1,400&display=swap">
<style>
  :root {
    --canvas-grey: #a7a7a7;
    --sky-top: #5d6f86;
    --sky-mid: #8d97a6;
    --sky-glow: #c89a72;
    --horizon: #5a3d2c;
    --ground: #0d0c0d;
    --title-white: #ffffff;
    --gold: #f5e4ae;
    --beige: #eadbb6;
    --body-ink: #111a38;
    --author-line: #d9e2ee;
    --spine-veil: rgba(205, 214, 228, 0.28);
  }
  * { box-sizing: border-box; margin: 0; padding: 0; }
  html, body {
    width: 1200px; height: 906px; overflow: hidden;
    background: var(--canvas-grey);
  }
  .cover-spread {
    position: absolute; left: 54px; top: 99px;
    width: 1098px; height: 711px; overflow: hidden;
  }
  .sky-background {
    position: absolute; inset: 0;
    background:
      radial-gradient(ellipse 70% 30% at 55% 72%, rgba(230,160,100,0.55), transparent 70%),
      linear-gradient(180deg, var(--sky-top) 0%, var(--sky-mid) 35%, #9c9a9c 55%, var(--sky-glow) 70%, var(--horizon) 80%, var(--ground) 88%, var(--ground) 100%);
  }
  /* Back cover */
  .back-cover { position: absolute; left: 0; top: 0; width: 518px; height: 711px; }
  .back-title {
    position: absolute; left: 0; width: 518px; top: 34px; text-align: center;
    font-family: "Tinos", serif; font-weight: 700; font-size: 26px; color: var(--gold);
  }
  .back-subtitle {
    position: absolute; left: 0; width: 518px; top: 68px; text-align: center;
    font-family: "Tinos", serif; font-weight: 700; font-size: 21px; line-height: 27px; color: var(--gold);
  }
  .back-copy {
    position: absolute; left: 44px; top: 150px; width: 446px;
    font-family: "Tinos", serif; font-size: 13.4px; line-height: 15.6px; color: var(--body-ink);
  }
  .back-copy p { margin-bottom: 14px; text-align: justify; }
  .author-photo {
    float: left; width: 88px; height: 140px; margin: 38px 14px 4px 28px;
    background: linear-gradient(180deg, #c6b8a6 0%, #33405e 55%, #1f2a45 100%);
    border-radius: 44px 44px 8px 8px;
  }
  .isbn {
    position: absolute; left: 285px; top: 545px;
    font-family: "Roboto Condensed", sans-serif; font-size: 14px; color: var(--title-white);
  }
  .barcode-area { position: absolute; left: 285px; top: 572px; width: 202px; height: 117px; background: #fff; }
  .publisher-mark {
    position: absolute; left: 34px; top: 610px; display: flex; align-items: center; gap: 8px;
  }
  .publisher-mark .square { width: 22px; height: 22px; background: #d5dbe6; }
  .publisher-name {
    font-family: "Roboto Condensed", sans-serif; font-weight: 400; font-size: 11px; line-height: 13px; color: var(--title-white);
  }
  .website {
    position: absolute; left: 80px; top: 672px;
    font-family: "Tinos", serif; font-style: italic; font-size: 14px; color: #f0e2c0;
  }
  /* Spine */
  .spine {
    position: absolute; left: 518px; top: 0; width: 63px; height: 711px;
    background: var(--spine-veil);
    border-left: 1px solid rgba(255,255,255,0.25); border-right: 1px solid rgba(255,255,255,0.25);
  }
  .spine-title {
    position: absolute; left: 8px; top: 18px; writing-mode: vertical-rl;
    font-family: "Oswald", sans-serif; font-weight: 700; font-size: 25px; letter-spacing: 1px; color: var(--title-white);
  }
  .spine-subtitle {
    position: absolute; left: 36px; top: 18px; writing-mode: vertical-rl;
    font-family: "Roboto Condensed", sans-serif; font-size: 14.5px; color: #eef1f6;
  }
  .spine-authors {
    position: absolute; left: 0; width: 61px; top: 593px; padding-top: 10px; text-align: center;
    border-top: 3px solid #9ea8c9;
    font-family: "Roboto Condensed", sans-serif; font-size: 13px; line-height: 15px; color: var(--title-white);
  }
  .spine-mark { position: absolute; left: 21px; top: 672px; width: 20px; height: 20px; background: #d5dbe6; }
  /* Front cover */
  .front-cover { position: absolute; left: 581px; top: 0; width: 517px; height: 711px; }
  .author-line {
    position: absolute; left: 0; width: 517px; top: 20px; text-align: center;
    font-family: "Roboto Condensed", sans-serif; font-weight: 300; font-size: 15.5px; color: var(--author-line);
  }
  .front-title {
    position: absolute; right: 32px; top: 118px; text-align: right;
    font-family: "Oswald", sans-serif; font-weight: 700; font-size: 96px; line-height: 101px;
    color: var(--title-white); letter-spacing: 1px;
  }
  .front-subtitle {
    position: absolute; right: 36px; top: 620px; text-align: right;
    font-family: "Roboto Condensed", sans-serif; font-weight: 300; color: var(--beige);
  }
  .front-subtitle .lead { font-size: 22px; line-height: 26px; display: block; }
  .front-subtitle .lead b { font-weight: 400; font-size: 24px; }
  .front-subtitle .tail { font-size: 17px; line-height: 20px; display: block; }
</style>
</head>
<body>
<main class="cover-spread">
  <div class="sky-background" role="img" aria-label="Full-bleed photograph of an evening sky with clouds and a warm sunset glow over dark hills"></div>

  <section class="back-cover">
    <h2 class="back-title">Growing Older Wisely</h2>
    <p class="back-subtitle">A Handy Compact Manual<br>for Legal, Financial and Emotional Health</p>
    <div class="back-copy">
      <p>Death and taxes may be inevitable, but they both require a lot of preparation. Fifty percent of America’s seventy-four million baby boomers have parents eighty or older, and nearly half of those boomers haven’t discussed end-of-life issues with their loved ones.</p>
      <p>In Growing Older Wisely, the authors present a detailed, step-by-step guide on how to deal with aging. They tackle issues such as wills and trusts, estate planning, senior housing, caregiving, hospice care, and death and bereavement. Their approach is lighthearted but thorough, and they provide a sorely needed examination of all the details involved in growing old in America.</p>
      <p><span class="author-photo" role="img" aria-label="Portrait photograph of author Renata L. Voss"></span><b>Renata L. Voss</b> is a social services administrator, and Contributor Martin K. Alder is an attorney. They have combined their skills and knowledge to give readers a practical understanding of the issues involved in caring for an elderly family member. Renata L. Voss holds an advanced degree in Public Administration from Harbor State University and is currently an Administrator at the Westfield County Department of Social Services. Collaborator Martin K. Alder is an attorney who has practiced for thirty-five years in the areas of family law, wills, trusts, and estate planning. In Growing Older Wisely, the two have pooled their expertise to provide an invaluable guide to all the issues involved in caring for a loved one at the end of his or her life.</p>
    </div>
    <div class="isbn">ISBN: 978-0-000-41852-6</div>
    <div class="barcode-area"></div>
    <div class="publisher-mark">
      <div class="publisher-name">NINE LANTERNS QUILL HOUSE<br>An Imprint of Nine Lanterns</div>
      <span class="square"></span>
    </div>
    <div class="website">www.renatavosswrites.com</div>
  </section>

  <section class="spine">
    <div class="spine-title">GROWING OLDER WISELY</div>
    <div class="spine-subtitle">A Handy Compact MANUAL for Legal, Financial and Emotional Health</div>
    <div class="spine-authors">VOSS<br>with<br>ALDER</div>
    <span class="spine-mark"></span>
  </section>

  <section class="front-cover">
    <p class="author-line">RENATA L. VOSS, M.P.A. with MARTIN K. ALDER, ESQ.</p>
    <h1 class="front-title">GROWING<br>OLDER<br>WISELY</h1>
    <p class="front-subtitle">
      <span class="lead">A Handy Compact <b>MANUAL</b></span>
      <span class="tail">for Legal, Financial and Emotional Health</span>
    </p>
  </section>
</main>
</body>
</html>
```